Business card design for an Art Director working for museums

The business card design we're looking for is for an Art Director in a private museum called "OLV Gallery". The museum showcases artworks made by the country's national artists. Designs should use the CMYK "0 40 100 20". You have the liberty to use any type you want except for overly decorative ones.

Target Market(s)

Professional and creative individuals. Interior designers, museum curators, museum coordinators etc

Industry/Entity Type

Museum

Contact Information for Business Card

Rel T
Art Director
+1 555 374 9281

Font styles to use
Serif
Sans Serif
Script

Requirements
Must have
• My project must have the CMYK 0 40 100 20. You can play with the Key.
• We're keen on clean, minimal, and architectural-type design.
Nice to have
• Geometric gradients that nicely complement the main CMYK that we've posted.
Should not have
• Off-putting colour palettes

```html
<!DOCTYPE html>
<html lang="en">
<head>
<meta charset="utf-8">
<title>OLV Gallery – Business Card</title>
<link rel="stylesheet" href="https://fonts.googleapis.com/css2?family=Federo&family=Marcellus&display=swap">
<style>
  :root {
    --amber: #d18f2e;
    --amber-soft: #dba253;
    --ink: #3a3a3a;
    --grey-light: #e6e6e6;
    --grey-mid: #9a9a9a;
    --grey-dark: #5e5e5e;
    --paper: #ffffff;
    --backdrop: #ebe8e3;
  }
  * { margin: 0; padding: 0; box-sizing: border-box; }
  html, body { width: 1200px; height: 702px; overflow: hidden; }
  body { background: var(--backdrop); position: relative; }

  .card {
    position: absolute;
    width: 520px;
    height: 300px;
    box-shadow: 0 6px 18px rgba(0,0,0,0.18);
    overflow: hidden;
  }
  .card svg { position: absolute; inset: 0; display: block; width: 100%; height: 100%; }

  .card--front { left: 70px; top: 60px; background: var(--amber); }
  .card--back  { left: 610px; top: 342px; background: var(--paper); }

  .identity {
    position: absolute;
    right: 38px;
    top: 156px;
    text-align: right;
    color: var(--ink);
  }
  .identity__org {
    font-family: "Federo", sans-serif;
    font-size: 36px;
    letter-spacing: 0.5px;
    line-height: 1;
    margin-bottom: 14px;
  }
  .identity__role,
  .identity__phone {
    font-family: "Marcellus", serif;
    font-size: 15px;
    line-height: 1.5;
  }
</style>
</head>
<body>

<div class="card card--front">
  <svg viewBox="0 0 520 300" xmlns="http://www.w3.org/2000/svg">
    <defs>
      <linearGradient id="front-fade" x1="0" y1="0" x2="1" y2="1">
        <stop offset="0" stop-color="var(--grey-dark)"/>
        <stop offset="0.5" stop-color="var(--grey-mid)"/>
        <stop offset="1" stop-color="var(--grey-light)"/>
      </linearGradient>
    </defs>
    <polygon class="front-pattern-area" role="img"
             aria-label="Diagonal grey and white stripe pattern"
             points="0,0 390,0 100,300 0,300" fill="url(#front-fade)"/>
  </svg>
  <div class="identity">
    <div class="identity__org">OLV Gallery</div>
    <div class="identity__role">Rel T Art Director</div>
    <div class="identity__phone">+1 555 374 9281</div>
  </div>
</div>

<div class="card card--back">
  <svg viewBox="0 0 520 300" xmlns="http://www.w3.org/2000/svg">
    <defs>
      <linearGradient id="back-fade" x1="0" y1="0" x2="1" y2="0.6">
        <stop offset="0" stop-color="var(--grey-dark)"/>
        <stop offset="0.3" stop-color="var(--grey-mid)"/>
        <stop offset="0.5" stop-color="var(--amber)"/>
        <stop offset="0.7" stop-color="var(--grey-mid)"/>
        <stop offset="1" stop-color="var(--grey-light)"/>
      </linearGradient>
    </defs>
    <rect class="back-pattern-area" role="img"
          aria-label="Angular geometric pattern of black, grey and amber diagonal bands"
          x="0" y="0" width="520" height="300" fill="url(#back-fade)"/>
  </svg>
</div>

</body>
</html>
```